Brevanta needs a business Card Design

We are looking for a business card Design for our new Managed Service Provider Company, Brevanta. Brevanta encompasses everything IT for the average medium sized business. Our primary services are help desk support, cyber-security (malware and ransomware protection), and Disaster Recovery systems. We would like the design to have a very clean and professional look, with a very minimalist feel.

Target Market(s)

Medium to large sized businesses

Industry/Entity Type

It Service

Contact Information for Business Card

Name GoesHere
name@brevanta-mail.net
O: 555-382-6047
C: 555-000-0000

Font styles to use
Other font styles liked:
• Poppins Font Only Please

Colors

Designer to choose only greyscale colors for use in the design.

Requirements
Must have
• Logo included
Nice to have
• Cutting Edge, innovative, minimalistic, elegant

```html
<!DOCTYPE html>
<html lang="en">
<head>
<meta charset="utf-8">
<title>Brevanta Business Card</title>
<link rel="stylesheet" href="https://fonts.googleapis.com/css2?family=Poppins:wght@300;400;500&display=swap">
<style>
  :root {
    --stage: #031a2c;
    --card-dark: #06233b;
    --card-light: #ffffff;
    --ink: #16243a;
    --ink-soft: #2b3445;
    --on-dark: #ffffff;
    --faint: #e7e7ec;
  }
  * { margin: 0; padding: 0; box-sizing: border-box; }
  html, body {
    width: 1200px; height: 1020px; overflow: hidden;
    background: var(--stage);
    font-family: "Poppins", sans-serif;
  }
  .canvas { position: relative; width: 1200px; height: 1020px; }
  .card {
    position: absolute; left: 271px; width: 657px;
    border-radius: 23px; overflow: hidden;
  }
  .card-front { top: 88px; height: 377px; background: var(--card-dark); }
  .card-back { top: 514px; height: 375px; background: var(--card-light); }

  .front-brand {
    position: absolute; left: 0; right: 0; top: 125px;
    display: flex; flex-direction: column; align-items: center;
  }
  .front-brand .brand-dot {
    width: 22px; height: 22px; border-radius: 50%;
    background: var(--on-dark); margin-bottom: 50px;
  }
  .front-brand .brand-name {
    color: var(--on-dark); font-weight: 300; font-size: 30px;
    letter-spacing: 0.5em; margin-right: -0.5em; line-height: 1;
  }

  .back-decor {
    position: absolute; left: 430px; top: 50px;
    width: 300px; height: 300px; border-radius: 50%;
    background: var(--faint);
  }
  .back-brand {
    position: absolute; left: 22px; top: 52px;
    display: flex; flex-direction: column; align-items: center;
  }
  .back-brand .brand-dot {
    width: 14px; height: 14px; border-radius: 50%;
    background: var(--ink); margin-bottom: 34px;
  }
  .back-brand .brand-name {
    color: var(--ink); font-weight: 400; font-size: 17px;
    letter-spacing: 0.5em; line-height: 1;
  }
  .holder { position: absolute; left: 22px; top: 193px; }
  .holder-name { color: var(--ink); font-weight: 500; font-size: 27px; line-height: 1.1; }
  .holder-role { color: var(--ink-soft); font-weight: 400; font-size: 18px; line-height: 1.2; }

  .contacts { position: absolute; left: 22px; top: 262px; list-style: none; }
  .contacts li {
    display: flex; align-items: center; height: 23px;
    color: var(--ink); font-size: 18px; font-weight: 400;
  }
  .contacts svg { width: 14px; height: 14px; margin-right: 8px; flex: none; }
</style>
</head>
<body>
<div class="canvas">
  <section class="card card-front">
    <div class="front-brand">
      <span class="brand-dot"></span>
      <span class="brand-name">BREVANTA</span>
    </div>
  </section>

  <section class="card card-back">
    <div class="back-decor"></div>
    <div class="back-brand">
      <span class="brand-dot"></span>
      <span class="brand-name">BREVANTA</span>
    </div>
    <div class="holder">
      <p class="holder-name">Jordan Hale</p>
      <p class="holder-role">Founder</p>
    </div>
    <ul class="contacts">
      <li>
        <svg viewBox="0 0 14 14"><rect x="3" y="0.8" width="8" height="12.4" rx="1.3" fill="none" stroke="#16243a" stroke-width="1.4"/><rect x="6" y="10.5" width="2" height="1" fill="#16243a"/></svg>
        555-000-0000
      </li>
      <li>
        <svg viewBox="0 0 14 14"><path d="M3 1.5l2.2 2.6-1.2 1.6c.8 1.8 2.3 3.3 4.1 4.1l1.6-1.2 2.6 2.2-1.4 1.8C6.2 12.4 1.6 7.8 1.2 3z" fill="#16243a"/></svg>
        555-382-6047
      </li>
      <li>
        <svg viewBox="0 0 14 14"><rect x="1" y="3" width="12" height="8.5" fill="#16243a"/><path d="M1.5 3.5L7 8l5.5-4.5" fill="none" stroke="#fff" stroke-width="1"/></svg>
        name@brevanta-mail.net
      </li>
      <li>
        <svg viewBox="0 0 14 14"><circle cx="7" cy="7" r="6" fill="#16243a"/><path d="M4 4.5c1 .3 1.5 1.2 1 2s.6 1.5 1.2 2.3M9 3c-.5 1 .3 1.6 1.3 1.8M8.5 11c0-1 .8-1.6 1.8-1.8" fill="none" stroke="#fff" stroke-width="1"/></svg>
        www.brevanta-mail.net
      </li>
    </ul>
  </section>
</div>
</body>
</html>
```